" A empresa tem como principal atrativo a grande variedade de joias infantis. Nosso maior diferencial são as peças de alta joalheria para crianças e a confecção de joias exclusivas e personalizadas para o publico de todas as idades. Temos um atelier para atendimento com hora marcada e o e-commerce é nossa principal vitrine. É possível conhecer algumas peças e parte da identidade da marca no nosso site www.brilhomirim.com.br e no instagram @brilhomirim "

```html
<!DOCTYPE html>
<html lang="pt-BR">
<head>
<meta charset="utf-8">
<title>Brilho Mirim — Cartão Fidelidade</title>
<link rel="stylesheet" href="https://fonts.googleapis.com/css2?family=Cormorant+Garamond:wght@500&family=Open+Sans:wght@700&display=swap">
<style>
  :root {
    --backdrop: #efe4d4;
    --card-white: #ffffff;
    --brand-blue: #6ec3dc;
    --card-blue: #90d2ea;
    --text-muted: #7d9aa5;
    --stamp-white: #ffffff;
    --watermark: rgba(255, 255, 255, 0.22);
  }
  html, body {
    margin: 0;
    padding: 0;
    width: 1200px;
    height: 1200px;
    overflow: hidden;
    background: var(--backdrop);
  }
  .canvas {
    position: relative;
    width: 1200px;
    height: 1200px;
  }
  .card {
    position: absolute;
    left: 276px;
    width: 617px;
    height: 334px;
    border-radius: 24px;
    box-shadow: 0 6px 18px rgba(90, 60, 30, 0.18);
    overflow: hidden;
  }
  /* Front */
  .card-front {
    top: 233px;
    background: var(--card-white);
  }
  .accent-bar {
    position: absolute;
    left: 50%;
    transform: translateX(-50%);
    width: 216px;
    height: 6px;
    border-radius: 3px;
    background: var(--brand-blue);
  }
  .accent-bar.top { top: 6px; }
  .accent-bar.bottom { bottom: 6px; }
  .brand-name {
    position: absolute;
    top: 118px;
    left: 0;
    right: 0;
    text-align: center;
    font-family: "Cormorant Garamond", serif;
    font-weight: 500;
    font-size: 52px;
    letter-spacing: 2px;
    color: var(--brand-blue);
    margin: 0;
  }
  .card-title {
    position: absolute;
    top: 275px;
    left: 0;
    right: 0;
    text-align: center;
    font-family: "Cormorant Garamond", serif;
    font-weight: 500;
    font-size: 31px;
    letter-spacing: 1.5px;
    color: var(--text-muted);
    margin: 0;
  }
  /* Back */
  .card-back {
    top: 643px;
    background: var(--card-blue);
  }
  .card-slot {
    position: absolute;
    left: 0;
    top: 96px;
    width: 14px;
    height: 172px;
    background: var(--card-white);
    border-radius: 0 6px 6px 0;
  }
  .watermark {
    position: absolute;
    top: 118px;
    left: 0;
    right: 0;
    text-align: center;
    font-family: "Cormorant Garamond", serif;
    font-weight: 500;
    font-size: 80px;
    letter-spacing: 3px;
    color: var(--watermark);
  }
  .stamps {
    position: absolute;
    left: 110px;
    top: 84px;
    display: grid;
    grid-template-columns: repeat(4, 72px);
    column-gap: 38px;
    row-gap: 24px;
  }
  .stamp {
    width: 72px;
    height: 72px;
    border-radius: 50%;
    background: var(--stamp-white);
  }
  .client-field {
    position: absolute;
    left: 65px;
    top: 276px;
    display: flex;
    align-items: flex-end;
    font-family: "Open Sans", sans-serif;
    font-weight: 700;
    font-size: 22px;
    color: var(--stamp-white);
  }
  .client-line {
    width: 406px;
    height: 2px;
    margin-left: 6px;
    margin-bottom: 5px;
    background: var(--stamp-white);
  }
</style>
</head>
<body>
<main class="canvas">
  <section class="card card-front" aria-label="Frente do cartão fidelidade">
    <span class="accent-bar top"></span>
    <h1 class="brand-name">BRILHO MIRIM</h1>
    <p class="card-title">CARTÃO FIDELIDADE</p>
    <span class="accent-bar bottom"></span>
  </section>

  <section class="card card-back" aria-label="Verso do cartão fidelidade">
    <span class="card-slot"></span>
    <div class="watermark" aria-hidden="true">BRILHO MIRIM</div>
    <div class="stamps">
      <span class="stamp"></span><span class="stamp"></span><span class="stamp"></span><span class="stamp"></span>
      <span class="stamp"></span><span class="stamp"></span><span class="stamp"></span><span class="stamp"></span>
    </div>
    <div class="client-field">Cliente:<span class="client-line"></span></div>
  </section>
</main>
</body>
</html>
```